Updated flyer

we are a defence industry trainer and we are updating a course that has been running for a few years, so want a new look flyer. Please note that the flyer is A4 and we would like people to fill in the document online. Please add a tickbox for SME's free and add a call out box saying the course is NEW & UPDATED.

Industry/Entity Type

Defence

Font styles to use
Sans Serif
Other font styles liked:
• AVENIR

Colors
3176b5
01a88e
9bcb3b
fbed22
f37022

```html
<!DOCTYPE html>
<html lang="en">
<head>
<meta charset="utf-8">
<title>Defence, ITAR &amp; EAR Training Flyer</title>
<link href="https://fonts.googleapis.com/css2?family=Source+Sans+3:ital,wght@0,400;0,600;0,700;1,400&display=swap" rel="stylesheet">
<style>
:root{
  --green:#8dc63f;
  --green-light:#a6d35a;
  --green-dark:#2d6a2f;
  --ink:#2b2b2b;
  --ink-soft:#555;
  --blue:#1f9ad6;
  --backdrop:#e9e9e6;
  --paper:#ffffff;
  --line:#c9e3a2;
}
*{box-sizing:border-box;margin:0;padding:0}
html,body{width:1200px;height:849px;overflow:hidden}
body{background:var(--backdrop);font-family:"Source Sans 3",Arial,sans-serif;color:var(--ink);position:relative}
.sheet{position:absolute;top:141px;width:400px;height:566px;background:var(--paper);box-shadow:0 4px 14px rgba(0,0,0,.18);overflow:hidden}
.sheet--front{left:170px}
.sheet--back{left:630px}
.abs{position:absolute}

/* brand */
.brand{display:flex;align-items:center;gap:6px}
.brand__dot{width:26px;height:26px;border-radius:50%;background:var(--green)}
.brand__name{font-weight:700;font-size:10.5px;line-height:1.05;color:var(--green-dark);text-transform:uppercase;width:86px}

/* front */
.front__band{left:0;top:0;width:400px;height:250px}
.front__brand{left:18px;top:26px}
.front__badge{right:22px;top:62px;text-align:right;font-weight:700;font-size:15px;line-height:1.05;color:var(--green-dark);text-transform:uppercase}
.front__title{left:20px;top:132px;width:360px;text-align:center;color:#fff;font-weight:700;font-size:17px;line-height:1.12;text-transform:uppercase}
.schedule{left:68px;top:190px;width:264px;height:90px;background:var(--green-light);border:2px solid #fff;border-radius:10px;display:flex;align-items:center;padding:0 14px;color:#fff;font-size:9.5px;line-height:1.35;letter-spacing:.04em;text-transform:uppercase}
.schedule__col{flex:1}
.schedule__col--dates{border-left:1px solid #fff;padding-left:16px}
.front__body{left:22px;top:296px;width:356px;font-size:8px;line-height:1.35;color:var(--ink)}
.front__body p{margin-bottom:6px}
.front__body strong{color:var(--green-dark)}
.price{left:0;top:392px;width:400px;text-align:center;color:var(--blue);font-weight:700;font-size:13px}
.price small{font-size:7px;font-weight:600}
.sme{left:0;top:414px;width:400px;text-align:center;color:var(--green);font-weight:700;font-size:9.5px}
.subsidy{left:0;top:430px;width:400px;text-align:center;font-size:10.5px;color:var(--ink)}
.footer-bar{left:0;bottom:0;width:400px;height:20px;background:var(--green-dark);color:#fff;font-size:7.5px;font-weight:600;display:flex;align-items:center;justify-content:center;gap:14px}

/* back */
.back__brand{left:18px;top:28px}
.back__title{left:200px;top:16px;width:185px;color:var(--green);font-weight:700;font-size:10px;line-height:1.1;text-transform:uppercase}
.bar{height:13px;background:var(--green);color:#fff;font-weight:700;font-size:8.5px;line-height:13px;text-align:center}
.course{left:16px;top:92px;width:178px}
.course__list{margin-top:4px;list-style:none;font-size:6px;line-height:8.2px;color:var(--ink)}
.course__list li{padding-left:7px;position:relative}
.course__list li::before{content:"";position:absolute;left:0;top:2.7px;width:3px;height:3px;background:var(--ink);border-radius:50%}
.register{left:204px;top:68px;width:182px}
.form{margin-top:5px;font-size:6px;color:var(--ink)}
.field{display:flex;align-items:center;height:9px;margin-bottom:1.5px}
.field__label{width:58px;flex:none}
.field__box{flex:1;height:7px;background:var(--line)}
.field__note{white-space:nowrap}
.checks{display:flex;gap:8px;align-items:center;height:10px}
.check{display:flex;align-items:center;gap:2px}
.check::before{content:"";width:5px;height:5px;border:.7px solid var(--ink)}
.form__note{font-size:5.6px;margin-top:2px}
.other{left:204px;top:262px;width:182px}
.other__text{font-size:6px;line-height:8px;margin-top:4px}
.office{left:204px;top:306px;width:182px}
.office__row{display:flex;gap:6px;margin-top:6px;font-size:5.6px}
.office__row span{flex:1;border-bottom:.7px dotted var(--ink-soft);padding-bottom:1px}
.quotes{left:0;top:388px;width:400px;height:80px;background:var(--green);color:#fff;font-style:italic;font-size:8.5px;line-height:1.2}
.quote{position:absolute;width:92px}
.cancel{left:16px;top:494px;width:368px;font-size:6.2px;line-height:1.35}
.cancel strong{color:var(--green-dark)}
.back__footer{justify-content:space-between;padding:0 14px;height:24px}
</style>
</head>
<body>

<section class="sheet sheet--front" aria-label="Flyer front">
  <svg class="abs front__band" viewBox="0 0 400 250" aria-hidden="true">
    <rect x="0" y="40" width="400" height="210" fill="#8dc63f"/>
    <path d="M0 0 H400 V40 C300 40 250 52 200 82 C150 108 70 112 0 108 Z" fill="#ffffff"/>
    <path d="M0 108 C70 112 150 108 200 82 C250 52 300 40 400 40 V46 C300 46 255 60 205 88 C150 116 70 118 0 114 Z" fill="#d8d8d8"/>
  </svg>
  <div class="abs brand front__brand">
    <span class="brand__dot"></span>
    <span class="brand__name">Northgate Trade Compliance</span>
  </div>
  <div class="abs front__badge">New<br>Updated</div>
  <h1 class="abs front__title">Defence, ITAR &amp; EAR Training Controls from a non-U.S. Perspective Training</h1>

  <div class="abs schedule">
    <div class="schedule__col">Brisbane<br>Sydney<br>Canberra<br>Melbourne<br>Adelaide</div>
    <div class="schedule__col schedule__col--dates">16 &amp; 17 March<br>18 &amp; 19 March<br>20 &amp; 23 March<br>24 &amp; 25 March<br>26 &amp; 27 March</div>
  </div>

  <div class="abs front__body">
    <p><strong>U.S. Export Controls</strong> are some of the most complex and stringent in the world. The U.S. Government regulates the transfer of U.S. origin goods and technical data throughout the world, with the intent of preventing unauthorised transfer of technology and know how. These controls extend world-wide and can impact anyone dealing in U.S. controlled goods or technology.</p>
    <p><strong>This two-day comprehensive course</strong> will give applicants a greater understanding of U.S. Export Controls from a non-U.S. perspective in practical and relevant terms.</p>
  </div>
  <div class="abs price">$1295.00 AUD per person <small>inc GST</small></div>
  <div class="abs sme">Small to Medium Enterprises FREE OF CHARGE</div>
  <div class="abs subsidy">Subsidised by the Regional Industry Growth Office (RIGO)</div>
  <div class="abs footer-bar">For more information, please contact NTC on +61 (0)7 5550 0142 or info@northgatetc.com.au</div>
</section>

<section class="sheet sheet--back" aria-label="Flyer back">
  <div class="abs brand back__brand">
    <span class="brand__dot"></span>
    <span class="brand__name">Northgate Trade Compliance</span>
  </div>
  <h2 class="abs back__title">Defence, ITAR &amp; EAR Training Controls from a non-U.S. Perspective Training</h2>

  <div class="abs course">
    <div class="bar">2 Day Course Content</div>
    <ul class="course__list">
      <li>Export Control terms and conditions</li>
      <li>Export Control Reform and the impact to Australian industry</li>
      <li>Managing reclassifications</li>
      <li>Applying definitions</li>
      <li>Understanding 600 Series &amp; limitations</li>
      <li>Understanding the Commerce Country List, Country Chart &amp; Country Groups</li>
      <li>Understanding deemed exports</li>
      <li>EAR General Prohibitions</li>
      <li>Understanding jurisdictions</li>
      <li>U.S. export controls jurisdiction</li>
      <li>Relevant legislation</li>
      <li>U.S. exemptions &amp; requirements</li>
      <li>Understand U.S. authorisations</li>
      <li>Reexports, retransfers &amp; how to obtain authorisation</li>
      <li>Applying U.S. exemptions</li>
      <li>Understanding re-exports</li>
      <li>Australian export controls</li>
      <li>Australia / U.S. Trade Co-operation Treaty</li>
      <li>Dual &amp; third country national issues &amp; exemptions</li>
      <li>Developing a compliance framework</li>
      <li>Cloud computing &amp; other technical issues</li>
      <li>Managing multi-jurisdictions</li>
      <li>Identifying the best authorisations to use</li>
      <li>Record keeping &amp; administrative requirements</li>
      <li>Understanding TAAs</li>
      <li>Creating a monitoring &amp; self-assessment process</li>
      <li>Managing violations</li>
      <li>Case studies</li>
      <li>Non-compliance &amp; fines</li>
      <li>Best practice principles</li>
      <li>Strategic planning</li>
    </ul>
  </div>

  <div class="abs register">
    <div class="bar">Register Below</div>
    <form class="form">
      <div class="field"><span class="field__label">Name:</span><span class="field__box"></span></div>
      <div class="field"><span class="field__label">Company:</span><span class="field__box"></span></div>
      <div class="field"><span class="field__label">Address:</span><span class="field__box"></span></div>
      <div class="field"><span class="field__label">Mobile no:</span><span class="field__box"></span></div>
      <div class="field"><span class="field__label">Email:</span><span class="field__box"></span></div>
      <div class="field"><span class="field__label">Dietary needs:</span><span class="field__box"></span></div>
      <div class="field"><span class="field__note">Payment method: (please check one)</span></div>
      <div class="checks"><span class="check">Invoice</span><span class="check">Credit card</span><span class="check">Free of Charge (SME)</span></div>
      <div class="checks"><span class="field__label">Card type:</span><span class="check">Crestcard</span><span class="check">Paywell</span><span class="check">Orbitpay</span></div>
      <div class="field"><span class="field__label">Card name:</span><span class="field__box"></span></div>
      <div class="field"><span class="field__label">Card number:</span><span class="field__box"></span></div>
      <div class="field"><span class="field__label">Expiry date:</span><span class="field__box"></span></div>
      <div class="field"><span class="field__label">Cardholder email:</span><span class="field__box"></span></div>
      <p class="form__note">Credit card payments incur a 2.5% surcharge. Orbitpay incurs 3%.</p>
    </form>
  </div>

  <div class="abs other">
    <div class="bar">Other Ways To Register</div>
    <p class="other__text">online at www.northgatetc.com.au/register<br>email registrations to info@northgatetc.com.au<br>fax to +61 (0)7 5550 0143</p>
  </div>

  <div class="abs office">
    <div class="bar">Office Use Only</div>
    <div class="office__row"><span>Confirmation sent:</span><span>Invoice no:</span></div>
    <div class="office__row"><span>Contact person:</span><span>Paid:</span></div>
  </div>

  <div class="abs quotes">
    <p class="quote" style="left:16px;top:44px">“Excellent presenter and coordination.”</p>
    <p class="quote" style="left:112px;top:22px">“Excellent...best U.S export controls training I have attended.”</p>
    <p class="quote" style="left:112px;top:54px">“Very informative, well presented course.”</p>
    <p class="quote" style="left:212px;top:30px">“Practical workshops were fantastic.”</p>
    <p class="quote" style="left:300px;top:8px">“Excellent structure and style of presentation.”</p>
  </div>

  <p class="abs cancel"><strong>Cancellation Policy:</strong> Cancellations incur a 20% administration fee. No cancellations permitted within 10 days of training commencing. If a registered attendee is unable to attend, a replacement attendee is allowed.</p>

  <div class="abs footer-bar back__footer">
    <span>CONTACT:</span><span>t. +61 (0)7 5550 0142</span><span>e. info@northgatetc.com.au</span><span>www.northgatetc.com.au</span>
  </div>
</section>

</body>
</html>
```